Logo, Letterhead, Business Card Design for Information and Communication Technology company named Treluvo Technologies. We looking at the world class design to assist our company attract more clients.

Target Market(s)

Private and Government Customers. Age: 18-40,

Industry/Entity Type

Information Technology

Font styles to use
Sans Serif

Colors

Designer to choose colors to be used in the design.

Requirements
Must have
• Bright colours
Nice to have
• World class design
Should not have
• Green Colours

```html
<!DOCTYPE html>
<html lang="en">
<head>
<meta charset="utf-8">
<title>Treluvo Technologies — Stationery</title>
<link rel="stylesheet" href="https://fonts.googleapis.com/css2?family=Montserrat:wght@700&family=Roboto:wght@400;500;700&display=swap">
<style>
  :root{
    --orange:#e0861f;
    --orange-deep:#c8680a;
    --charcoal:#3a3a3a;
    --paper:#ffffff;
    --paper-soft:#f4f4f4;
    --stage:#8d8d8d;
    --ink:#2b2b2b;
  }
  *{box-sizing:border-box;margin:0;padding:0}
  html,body{width:1200px;height:981px;overflow:hidden}
  body{background:var(--stage);font-family:"Roboto",sans-serif;position:relative}
  .brand{font-family:"Montserrat",sans-serif;font-weight:700;color:var(--orange);display:flex;align-items:center;gap:10px;line-height:1}
  .brand-dot{width:14px;height:14px;border-radius:50%;background:var(--orange);flex:none}
  .brand-name{display:flex;flex-direction:column}
  .brand-name .word{letter-spacing:1px}
  .brand-name .sub{letter-spacing:.42em;margin-top:4px}

  .master-logo{position:absolute;left:40px;top:40px}
  .master-logo .word{font-size:58px}
  .master-logo .sub{font-size:17px}

  .sheet{position:absolute;background:var(--paper);box-shadow:0 8px 22px rgba(0,0,0,.28);overflow:hidden}

  /* letterhead */
  .letterhead{left:40px;top:150px;width:420px;height:594px}
  .letterhead .brand{position:absolute;left:28px;top:28px}
  .letterhead .word{font-size:30px}
  .letterhead .sub{font-size:9px}
  .top-band{position:absolute;right:0;top:80px;width:180px;height:34px;background:linear-gradient(90deg,var(--orange-deep),var(--orange))}
  .corner-tab{position:absolute;left:0;top:0;width:18px;height:50px;background:var(--orange)}
  .foot-band{position:absolute;left:0;right:0;bottom:56px;height:34px;background:var(--orange-deep);display:flex;align-items:center;gap:18px;padding-left:20px;color:#fff;font-size:10px;white-space:nowrap}
  .foot-band span::before{content:"";display:inline-block;width:6px;height:6px;border-radius:50%;background:#fff;margin-right:5px;vertical-align:middle}
  .corner-ornament{position:absolute;right:0;bottom:0;width:200px;height:56px;background:linear-gradient(90deg,var(--orange-deep),var(--orange))}

  /* envelope */
  .envelope{left:500px;top:600px;width:660px;height:330px;background:var(--paper-soft)}
  .envelope .brand{position:absolute;left:36px;top:34px}
  .envelope .word{font-size:32px}
  .envelope .sub{font-size:10px}
  .envelope .foot-band{bottom:80px;height:40px;font-size:13px;gap:26px}
  .envelope .corner-ornament{width:230px;height:80px}
  .recipient{position:absolute;right:40px;top:120px;text-align:right;font-size:12px;font-weight:700;font-style:normal;color:var(--ink);line-height:1.35;text-transform:uppercase}
  .recipient .attn{color:var(--orange);text-decoration:underline;margin-bottom:8px;font-weight:500}

  /* cards */
  .card{width:320px;height:185px}
  .card-back{left:500px;top:160px;background:var(--paper)}
  .card-front{left:860px;top:160px;background:var(--paper-soft)}
  .card-back .dark-panel{position:absolute;left:0;top:38px;width:170px;height:80px;background:var(--charcoal);display:flex;align-items:center;padding-left:14px}
  .card .word{font-size:22px}
  .card .sub{font-size:7px}
  .card .brand-dot{width:10px;height:10px}
  .card-back .fade{position:absolute;left:0;top:0;width:170px;height:38px;background:linear-gradient(90deg,#f1d7b3,#fff)}
  .contact-list{position:absolute;left:184px;top:42px;list-style:none;font-size:8px;color:var(--ink);line-height:1.35}
  .contact-list li{display:flex;gap:6px;align-items:flex-start;margin-bottom:6px}
  .contact-list svg{flex:none}
  .card-back .edge{position:absolute;right:10px;top:50px;width:6px;height:70px;background:var(--orange)}
  .card-front .stripe{position:absolute;left:0;top:60px;width:26px;height:70px;background:var(--orange)}
  .card-front .dark-panel{position:absolute;left:26px;top:60px;right:26px;height:70px;background:var(--charcoal);display:flex;align-items:center;justify-content:center}
</style>
</head>
<body>

<div class="brand master-logo">
  <span class="brand-dot"></span>
  <span class="brand-name"><span class="word">TRELUVO</span><span class="sub">TECHNOLOGIES</span></span>
</div>

<section class="sheet letterhead">
  <div class="corner-tab"></div>
  <div class="brand"><span class="brand-dot"></span><span class="brand-name"><span class="word">TRELUVO</span><span class="sub">TECHNOLOGIES</span></span></div>
  <div class="top-band"></div>
  <div class="foot-band"><span>www.treluvotech.net</span><span>hello@treluvo.net</span><span>0 310 482 957</span></div>
  <div class="corner-ornament" role="img" aria-label="Orange corner ornament of outlined hexagons"></div>
</section>

<section class="sheet card card-back">
  <div class="fade"></div>
  <div class="dark-panel"><div class="brand"><span class="brand-dot"></span><span class="brand-name"><span class="word">TRELUVO</span><span class="sub">TECHNOLOGIES</span></span></div></div>
  <ul class="contact-list">
    <li><svg width="12" height="12" viewBox="0 0 12 12"><circle cx="6" cy="6" r="6" fill="var(--orange)"/><path d="M4 3l1.2 1.6-.7.8a4 4 0 002 2l.8-.7L9 8 8 9.2A5 5 0 012.8 4z" fill="#fff"/></svg><span>031 0482 9571<br>031 0482 9572</span></li>
    <li><svg width="12" height="12" viewBox="0 0 12 12"><circle cx="6" cy="6" r="6" fill="var(--orange)"/><circle cx="6" cy="6" r="2.4" fill="none" stroke="#fff"/></svg><span>desk@treluvo.net<br>www.treluvotech.net</span></li>
    <li><svg width="12" height="12" viewBox="0 0 12 12"><circle cx="6" cy="6" r="6" fill="var(--orange)"/><path d="M6 2.5a2.3 2.3 0 00-2.3 2.3C3.7 6.6 6 9.5 6 9.5s2.3-2.9 2.3-4.7A2.3 2.3 0 006 2.5z" fill="#fff"/></svg><span>Harbor Lane 2,<br>Dunmere 40718</span></li>
  </ul>
  <div class="edge"></div>
</section>

<section class="sheet card card-front">
  <div class="stripe"></div>
  <div class="dark-panel"><div class="brand"><span class="brand-dot"></span><span class="brand-name"><span class="word">TRELUVO</span><span class="sub">TECHNOLOGIES</span></span></div></div>
</section>

<section class="sheet envelope">
  <div class="brand"><span class="brand-dot"></span><span class="brand-name"><span class="word">TRELUVO</span><span class="sub">TECHNOLOGIES</span></span></div>
  <address class="recipient"><div class="attn">Lorem ipsum dummy text for text to replace</div>Harbor Lane 2, Dunmere<br>Country 4321</address>
  <div class="foot-band"><span>www.treluvotech.net</span><span>hello@treluvo.net</span><span>0 310 482 957</span></div>
  <div class="corner-ornament" role="img" aria-label="Orange corner ornament of outlined hexagons"></div>
</section>

</body>
</html>
```